Vel-Trax.ch is looking for business card letterhead and envelope C5 with WOW effect

We need a strong business card for our company Vel-Trax.ch, logo is available. You want a black or dark background on which the logo Stark r% 26 # 252; appears. Letterhead and envelope in C5 format should be in a similar design, but does not have to be We need a strong business card for our company Vel-Trax.ch, logo is available. A black or dark background is desired, on which the logo Stark comes across. The letterhead and the envelope in C5 format should have a similar design.

Target Market(s)

Private customers as well as entrepreneurs

Contact Information for Business Card

E-mail: info@vel-trax.ch
Web.www.Vel-Trax.ch
Tel: +41 ( 0 ) 79 684 3027
Adresse:
Lindenhaldeweg 14
9418 Brenzikon

Hier kann man Icons verwenden für Email,Tel und Adressse

Font styles to use
Other font styles liked:
• Dubai,bold

Colors

Designer to choose colors to be used in the design.

Requirements
Must have
• WOW effect
Nice to have
• R% 26 # 252; back business card with our service listings. - VEHICLE LABELING - SHOP WINDOW LABELING - STICKERS AND MUCH MORE ... in red color

```html
<!DOCTYPE html>
<html lang="en">
<head>
<meta charset="utf-8">
<title>Vel-Trax.ch – Business Card</title>
<link rel="stylesheet" href="https://fonts.googleapis.com/css2?family=Arimo:wght@700&display=swap">
<style>
  :root {
    --backdrop: #8c8c8c;
    --card: #333333;
    --pattern-dark: #050505;
    --accent: #f7c600;
    --name: #ffffff;
    --icon: #bbbbbb;
    --icon-fill: #eeeeee;
    --font-main: "Arimo", Arial, sans-serif;
  }
  html, body {
    margin: 0;
    padding: 0;
    width: 1200px;
    height: 1200px;
    overflow: hidden;
    background: var(--backdrop);
  }
  .canvas {
    position: relative;
    width: 1200px;
    height: 1200px;
    font-family: var(--font-main);
  }
  .card {
    position: absolute;
    left: 246px;
    width: 707px;
    height: 400px;
    background: var(--card);
    overflow: hidden;
  }
  .card--front { top: 187px; }
  .card--back { top: 612px; }

  .pattern-area {
    position: absolute;
    inset: 0;
  }
  .card--front .pattern-area {
    background: radial-gradient(ellipse 300px 260px at 560px 250px, var(--pattern-dark) 0%, rgba(5,5,5,0.7) 50%, rgba(51,51,51,0) 100%);
  }
  .card--back .pattern-area {
    background: radial-gradient(ellipse 300px 260px at 170px 260px, var(--pattern-dark) 0%, rgba(5,5,5,0.7) 50%, rgba(51,51,51,0) 100%);
  }

  .brand-mark {
    position: absolute;
    border-radius: 50%;
    background: var(--accent);
  }
  .card--front .brand-mark {
    left: 80px;
    top: 110px;
    width: 160px;
    height: 160px;
  }
  .card--back .brand-mark {
    left: 40px;
    top: 40px;
    width: 64px;
    height: 64px;
  }

  .brand-name {
    position: absolute;
    margin: 0;
    color: var(--name);
    font-weight: 700;
    text-transform: uppercase;
    white-space: nowrap;
    line-height: 1;
  }
  .card--front .brand-name {
    left: 259px;
    top: 164px;
    font-size: 54px;
    letter-spacing: 1px;
  }
  .card--back .brand-name {
    left: 134px;
    top: 64px;
    font-size: 25px;
    letter-spacing: 0.5px;
  }

  .contact-frame {
    position: absolute;
    left: 300px;
    top: 36px;
    width: 380px;
    height: 330px;
  }

  .contact-group {
    position: absolute;
    left: 300px;
    width: 382px;
    text-align: center;
    color: var(--accent);
    font-weight: 700;
    font-size: 20px;
    line-height: 27px;
  }
  .contact-group--online { top: 80px; }
  .contact-group--office { top: 192px; }
  .contact-group p { margin: 0; }
  .contact-address { font-style: normal; padding-left: 14px; line-height: 26px; }

  .icon-row {
    display: flex;
    justify-content: center;
    gap: 8px;
    margin-bottom: 12px;
  }
  .icon {
    width: 22px;
    height: 22px;
  }
</style>
</head>
<body>
<div class="canvas">

  <section class="card card--front" aria-label="Business card front">
    <div class="pattern-area" role="img" aria-label="Decorative black honeycomb pattern"></div>
    <span class="brand-mark" aria-hidden="true"></span>
    <h1 class="brand-name">Vel-Trax.ch</h1>
  </section>

  <section class="card card--back" aria-label="Business card back">
    <div class="pattern-area" role="img" aria-label="Decorative black honeycomb pattern"></div>
    <span class="brand-mark" aria-hidden="true"></span>
    <h2 class="brand-name">Vel-Trax.ch</h2>

    <svg class="contact-frame" viewBox="0 0 380 330" aria-hidden="true">
      <polygon points="7,166 84,5 284,5 374,166 284,325 84,325"
               fill="none" stroke="var(--accent)" stroke-width="3"/>
      <polygon points="22,166 92,15 276,15 359,166 276,315 92,315"
               fill="none" stroke="var(--accent)" stroke-width="3"/>
    </svg>

    <div class="contact-group contact-group--online">
      <div class="icon-row">
        <svg class="icon" viewBox="0 0 22 22" aria-label="Web">
          <circle cx="11" cy="11" r="10" fill="none" stroke="var(--icon)" stroke-width="1.2"/>
          <circle cx="11" cy="11" r="6" fill="none" stroke="var(--icon)" stroke-width="1"/>
          <ellipse cx="11" cy="11" rx="2.6" ry="6" fill="none" stroke="var(--icon)" stroke-width="0.9"/>
          <line x1="5" y1="11" x2="17" y2="11" stroke="var(--icon)" stroke-width="0.9"/>
        </svg>
        <svg class="icon" viewBox="0 0 22 22" aria-label="Email">
          <circle cx="11" cy="11" r="10" fill="none" stroke="var(--icon)" stroke-width="1.2"/>
          <rect x="6" y="7.5" width="10" height="7" fill="var(--icon-fill)"/>
          <polyline points="6,7.5 11,11.5 16,7.5" fill="none" stroke="#333" stroke-width="1"/>
        </svg>
      </div>
      <p>info@vel-trax.ch</p>
      <p>www.Vel-Trax.ch</p>
    </div>

    <div class="contact-group contact-group--office">
      <div class="icon-row">
        <svg class="icon" viewBox="0 0 22 22" aria-label="Phone">
          <circle cx="11" cy="11" r="10" fill="none" stroke="var(--icon)" stroke-width="1.2"/>
          <path d="M5.5 9 Q11 5 16.5 9 L15 10.5 L13 9.5 L9 9.5 L7 10.5 Z" fill="var(--icon-fill)"/>
          <rect x="7" y="11" width="8" height="5" rx="1" fill="var(--icon-fill)"/>
        </svg>
        <svg class="icon" viewBox="0 0 22 22" aria-label="Address">
          <circle cx="11" cy="11" r="10" fill="none" stroke="var(--icon)" stroke-width="1.2"/>
          <path d="M11 5 A3.5 3.5 0 0 1 14.5 8.5 C14.5 11 11 14.5 11 14.5 C11 14.5 7.5 11 7.5 8.5 A3.5 3.5 0 0 1 11 5 Z" fill="none" stroke="var(--icon-fill)" stroke-width="1.2"/>
          <ellipse cx="11" cy="16" rx="4" ry="1.2" fill="none" stroke="var(--icon-fill)" stroke-width="1"/>
        </svg>
      </div>
      <p>+41 ( 0 ) 79 684&nbsp; 3027</p>
      <address class="contact-address">
        Lindenhaldeweg 14<br>9418 Brenzikon
      </address>
    </div>
  </section>

</div>
</body>
</html>
```